One page website for a Personal Injury Law Firm

Design and code a one page website in WordPress for the Darrow Law Firm, which is a a personal injury law firm located in Coral Gables, Florida. Please note: if you want to change the color pallete for the logo and for the web design , that is fine by me.

Target Market(s)

Those injured in accidents that need legal representation

Industry/Entity Type

Legal

Coding

Coded - Design and coding required

Number of Pages Required

1 page

Font styles to use
Other font styles liked:
• Montserrat

```html
<!DOCTYPE html>
<html lang="en">
<head>
<meta charset="utf-8">
<title>Darrow Law Firm | Personal Injury Attorneys in Coral Gables, Florida</title>
<link rel="stylesheet" href="https://fonts.googleapis.com/css2?family=Gilda+Display&family=Montserrat:wght@400;500;600;700&display=swap">
<style>
:root{
  --tan:#d4a574;
  --tan-dark:#c39260;
  --ink:#2b2b2b;
  --charcoal:#2e2e2e;
  --text:#4a4a4a;
  --cream:#faf4ee;
  --white:#ffffff;
  --serif:"Gilda Display", Georgia, serif;
  --sans:"Montserrat", Arial, sans-serif;
}
*{box-sizing:border-box;margin:0;padding:0}
html,body{width:1200px;height:5296px;overflow:hidden}
body{position:relative;background:var(--white);font-family:var(--sans);color:var(--text)}
.abs{position:absolute}
svg{display:block}

/* header */
.topbar{left:456px;top:0;width:744px;height:33px;background:var(--ink);clip-path:polygon(14px 0,100% 0,100% 100%,0 100%)}
.topbar .item{position:absolute;top:9px;font-size:12px;font-weight:500;color:var(--white);display:flex;align-items:center;gap:8px}
.topbar .cta{position:absolute;left:417px;top:0;width:187px;height:33px;background:var(--tan);color:var(--white);font-size:11px;font-weight:600;letter-spacing:.5px;display:flex;align-items:center;justify-content:center}
.brand{left:140px;top:44px;font-family:var(--serif);font-size:25px;color:var(--ink)}
.nav{top:58px;font-size:11.5px;font-weight:600;color:var(--ink);letter-spacing:.4px}

/* hero */
.hero-title{left:0;width:1200px;text-align:center;color:var(--white);font-family:var(--serif)}

/* shared */
.heading{font-family:var(--serif);color:var(--ink);font-weight:400}
.kicker{font-size:12.5px;font-weight:700;color:var(--ink)}
.body{font-size:12.6px;line-height:21px;color:var(--text)}
.btn{display:flex;align-items:center;justify-content:center;background:var(--tan);color:var(--white);font-size:11.5px;font-weight:600;letter-spacing:.6px;outline:1px solid var(--tan);outline-offset:3px}
.photo{overflow:hidden}

/* why choose */
.why{left:0;top:1346px;width:1200px;height:884px;background:var(--cream)}
.feature{width:300px;text-align:center}
.feature h3{font-family:var(--serif);font-weight:400;font-size:19px;line-height:23px;color:var(--ink);margin-top:26px}
.feature p{font-size:12.2px;line-height:19px;margin-top:10px}
.stories{left:170px;top:1948px;width:860px;text-align:center;font-size:12.2px;line-height:21px}
.stories p{margin-bottom:14px}

/* lists */
.point{display:flex;gap:10px}
.point .tick{flex:0 0 16px;height:16px;border-radius:50%;background:var(--tan);display:flex;align-items:center;justify-content:center;margin-top:1px}
.point h4{font-size:12.5px;font-weight:700;color:var(--ink);margin-bottom:8px}

/* practice */
.practice{left:0;top:2893px;width:1200px;height:662px}
.card{position:absolute;background:rgba(36,36,36,.92);display:flex;align-items:center;justify-content:space-between;padding:0 18px 0 22px;font-family:var(--serif);font-size:15px;line-height:18px;color:var(--white)}
.card.featured{background:var(--tan);flex-direction:column;align-items:flex-start;justify-content:flex-start;padding:20px 20px}

/* cta */
.cta-box{left:140px;top:4591px;width:920px;height:255px;border:2px solid var(--tan)}
.cta-item{position:absolute;display:flex;align-items:center;gap:14px;font-family:var(--serif);font-size:17px;color:var(--ink)}
.cta-item span.plain{font-family:var(--sans);font-size:14px}

/* footer */
.footer{left:0;top:4938px;width:1200px;height:358px;background:var(--charcoal)}
.fnav{top:5065px;font-size:11.5px;font-weight:600;color:var(--white);letter-spacing:.4px}
.fsep{top:5063px;color:#8a8a8a;font-size:12px}
.fcontact{top:5137px;display:flex;gap:14px;color:var(--white);font-size:13px;line-height:18px}
.fcircle{width:38px;height:38px;border-radius:50%;background:#4a4a4a;display:flex;align-items:center;justify-content:center;flex:0 0 38px}
.social{width:30px;height:30px;border-radius:50%;border:1.5px solid #9a9a9a;top:5246px}
</style>
</head>
<body>

<!-- HEADER -->
<div class="abs topbar">
  <div class="item" style="left:50px">
    <svg width="13" height="13" viewBox="0 0 24 24"><path d="M6.6 10.8a15 15 0 0 0 6.6 6.6l2.2-2.2a1 1 0 0 1 1-.25 11.4 11.4 0 0 0 3.6.6 1 1 0 0 1 1 1V20a1 1 0 0 1-1 1A17 17 0 0 1 3 4a1 1 0 0 1 1-1h3.5a1 1 0 0 1 1 1 11.4 11.4 0 0 0 .6 3.6 1 1 0 0 1-.25 1z" fill="#fff"/></svg>
    (305) 555 0148</div>
  <div class="item" style="left:203px">
    <svg width="15" height="11" viewBox="0 0 24 17"><rect x="1" y="1" width="22" height="15" rx="1" fill="none" stroke="#fff" stroke-width="2"/><path d="M1 1l11 8 11-8" fill="none" stroke="#fff" stroke-width="2"/></svg>
    info@darrowlawfirm.com</div>
  <div class="cta">FREE CONSULTATION</div>
</div>
<div class="abs brand">Darrow Law Firm</div>
<div class="abs nav" style="left:407px">HOME</div>
<div class="abs nav" style="left:506px">ABOUT US</div>
<div class="abs nav" style="left:630px">PRACTICE AREAS</div>
<div class="abs nav" style="left:801px">WHY CHOOSE US</div>
<div class="abs nav" style="left:971px">CONTACT US</div>

<!-- HERO -->
<svg class="abs" style="left:0;top:98px" width="1200" height="600" viewBox="0 0 1200 600" role="img" aria-label="Photo of an injured client in a neck brace reviewing documents with an attorney at an office desk">
  <defs>
    <linearGradient id="heroPhoto" x1="0" y1="0" x2="1" y2="0">
      <stop offset="0" stop-color="#8f8a82"/><stop offset=".35" stop-color="#6f665d"/><stop offset=".65" stop-color="#8c8781"/><stop offset="1" stop-color="#4f5255"/>
    </linearGradient>
    <linearGradient id="heroShade" x1="0" y1="0" x2="0" y2="1">
      <stop offset=".4" stop-color="#000" stop-opacity="0"/><stop offset="1" stop-color="#000" stop-opacity=".5"/>
    </linearGradient>
  </defs>
  <polygon points="0,0 1200,0 1200,455 600,520 0,455" fill="url(#heroPhoto)"/>
  <polygon points="0,0 1200,0 1200,455 600,520 0,455" fill="url(#heroShade)"/>
  <polygon points="0,455 600,520 1200,455 1200,490 600,568 0,490" fill="var(--tan)"/>
</svg>
<div class="abs hero-title" style="top:470px;font-size:36px">Concierge-Level Personal Injury</div>
<div class="abs hero-title" style="top:520px;font-size:42px">Representation in Miami, Florida</div>

<!-- ABOUT -->
<div class="abs" style="left:0;top:1079px;width:508px;height:267px;background:var(--tan)"></div>
<div class="abs" style="left:382px;top:775px;width:208px;height:437px;background:var(--ink)"></div>
<div class="abs photo" style="left:140px;top:785px;width:440px;height:427px;background:linear-gradient(180deg,#c88a72 0%,#d7a27b 25%,#5b5766 55%,#2d3140 100%)" role="img" aria-label="Photo of the Miami skyline at dusk with high-rise towers along the waterfront"></div>
<div class="abs" style="left:140px;top:1248px;width:52px;height:52px;border-radius:50%;background:var(--white);display:flex;align-items:center;justify-content:center">
  <svg width="22" height="22" viewBox="0 0 24 24"><path d="M6.6 10.8a15 15 0 0 0 6.6 6.6l2.2-2.2a1 1 0 0 1 1-.25 11.4 11.4 0 0 0 3.6.6 1 1 0 0 1 1 1V20a1 1 0 0 1-1 1A17 17 0 0 1 3 4a1 1 0 0 1 1-1h3.5a1 1 0 0 1 1 1 11.4 11.4 0 0 0 .6 3.6 1 1 0 0 1-.25 1z" fill="var(--tan)"/></svg>
</div>
<div class="abs" style="left:206px;top:1252px;font-size:11px;font-weight:500;color:var(--white);letter-spacing:.4px">CALL US NOW</div>
<div class="abs" style="left:206px;top:1270px;font-size:24px;font-weight:600;color:var(--white)">(305) 555 0148</div>
<div class="abs" style="left:436px;top:1287px;width:72px;height:1px;background:var(--white)"></div>

<h2 class="abs heading" style="left:660px;top:808px;font-size:37px">The Darrow Law Firm</h2>
<div class="abs kicker" style="left:660px;top:866px;font-size:12px">Justice. Recovery. A Better Future Starts Here.</div>
<p class="abs body" style="left:660px;top:890px;width:400px">At The Darrow Law Firm, we understand that suffering a personal injury can be life-altering-physically, emotionally, and financially. You may be unsure whether pursuing legal action is the right step. But in Florida, holding negligent parties accountable isn't just your right-it's often necessary to rebuild your life.</p>
<p class="abs body" style="left:660px;top:1034px;width:400px">We take a concierge-style approach to personal injury law, offering personalized attention, strategic advocacy, and relentless dedication to securing the maximum compensation you deserve. Our mission is not only to make you whole again but to help you build a brighter future-ensuring access to the best medical care, financial stability, and peace of mind for you and your loved ones.</p>
<div class="abs btn" style="left:663px;top:1242px;width:134px;height:38px">READ MORE</div>

<!-- WHY CHOOSE -->
<div class="abs why"></div>
<h2 class="abs heading" style="left:0;top:1466px;width:1200px;text-align:center;font-size:34px">Why Choose The Darrow Law Firm?</h2>
<div class="abs" style="left:0;top:1523px;width:1200px;text-align:center;font-size:12.5px;color:var(--ink)">Unmatched Experience. Proven Results. Relentless Advocacy.</div>

<div class="abs feature" style="left:130px;top:1572px">
  <svg width="140" height="166" viewBox="0 0 140 166" style="margin:0 auto"><polygon points="70,4 136,42 136,124 70,162 4,124 4,42" fill="none" stroke="var(--tan)" stroke-width="5"/>
    <g fill="none" stroke="var(--ink)" stroke-width="3"><rect x="42" y="58" width="14" height="50"/><rect x="58" y="58" width="14" height="50"/><rect x="74" y="58" width="14" height="50"/><path d="M90 62l12 -3 10 46 -12 3z"/><line x1="46" y1="70" x2="52" y2="70"/><line x1="62" y1="70" x2="68" y2="70"/><line x1="78" y1="70" x2="84" y2="70"/></g></svg>
  <h3>25+ Years of<br>Legal Mastery</h3>
  <p>We have successfully handled thousands of cases, fighting both for and against insurance companies. This unique dual experience gives us an insider advantage in every case we take on.</p>
</div>
<div class="abs feature" style="left:450px;top:1572px">
  <svg width="140" height="166" viewBox="0 0 140 166" style="margin:0 auto"><polygon points="70,4 136,42 136,124 70,162 4,124 4,42" fill="none" stroke="var(--tan)" stroke-width="5"/>
    <g fill="none" stroke="var(--ink)" stroke-width="3"><rect x="44" y="52" width="44" height="60" rx="3"/><rect x="56" y="46" width="20" height="10" rx="2"/><path d="M52 70l4 4 6 -7M52 86l4 4 6 -7"/><line x1="66" y1="72" x2="80" y2="72"/><line x1="66" y1="88" x2="76" y2="88"/><path d="M86 82l12 -5 12 5v10c0 9 -6 14 -12 17c-6 -3 -12 -8 -12 -17z" fill="#faf4ee"/><path d="M93 92l4 4 7 -8"/></g></svg>
  <h3>Extensive Knowledge of<br>Insurance Tactics</h3>
  <p>Having worked for insurance companies, we know their strategies, loopholes, and how to dismantle their defenses to maximize your settlement.</p>
</div>
<div class="abs feature" style="left:770px;top:1572px">
  <svg width="140" height="166" viewBox="0 0 140 166" style="margin:0 auto"><polygon points="70,4 136,42 136,124 70,162 4,124 4,42" fill="none" stroke="var(--tan)" stroke-width="5"/>
    <g fill="none" stroke="var(--ink)" stroke-width="3"><circle cx="70" cy="83" r="24" stroke-dasharray="8 4" stroke-width="6"/><circle cx="70" cy="83" r="15"/><path d="M75 76c-2 -3 -10 -3 -10 2c0 5 10 3 10 8c0 5 -8 5 -10 2M70 71v24"/><path d="M40 70a32 32 0 0 1 14 -16M100 96a32 32 0 0 1 -14 16"/></g></svg>
  <h3>Millions Recovered<br>for Clients</h3>
  <p>Our track record includes life-changing results.</p>
</div>

<div class="abs stories">
  <p>A client fell eight feet at a major sporting venue and suffered catastrophic injuries. We recovered compensation that covered all medical bills, paid off their home, and funded their children's college education.</p>
  <p>A client suffered a severe infection from a minor slip-and-fall injury in a Miami condo building. We resolved the case before filing a lawsuit, securing funds that allowed him to buy a new home, pay off debts, and provide private school tuition for his children.</p>
  <p>A fast-food restaurant's napkin dispenser fell on a customer's face, breaking her nose and leaving her permanently disfigured. We secured a settlement that covered plastic surgery, home renovations, and her daughter's college tuition.</p>
  <p>These are just a few examples of how we fight for our clients' futures—not just their cases.</p>
</div>

<!-- STRATEGY -->
<h2 class="abs heading" style="left:142px;top:2350px;font-size:36px">Our Strategy</h2>
<div class="abs kicker" style="left:142px;top:2405px">Aggressive, Client-Focused, and Results-Driven</div>
<div class="abs" style="left:140px;top:2438px;width:430px">
  <div class="point"><div class="tick"><svg width="9" height="9" viewBox="0 0 10 10"><path d="M1.5 5.2l2.3 2.3 4.7-5" fill="none" stroke="#fff" stroke-width="1.8"/></svg></div>
    <div><h4>Taking on Corporate Giants</h4><p class="body">We don't back down from big insurance companies, property management firms, or major corporations. We fight for justice-no matter how powerful the opposition.</p></div></div>
  <div class="point" style="margin-top:22px"><div class="tick"><svg width="9" height="9" viewBox="0 0 10 10"><path d="M1.5 5.2l2.3 2.3 4.7-5" fill="none" stroke="#fff" stroke-width="1.8"/></svg></div>
    <div><h4>Concierge-Style Legal Care</h4><p class="body">You're not just another case number. We provide dedicated, personalized service, keeping you informed, supported, and empowered throughout the legal process.</p></div></div>
  <div class="point" style="margin-top:22px"><div class="tick"><svg width="9" height="9" viewBox="0 0 10 10"><path d="M1.5 5.2l2.3 2.3 4.7-5" fill="none" stroke="#fff" stroke-width="1.8"/></svg></div>
    <div><h4>No Win, No Fee Guarantee</h4><p class="body">We take your case on a contingency basis, which means you pay nothing unless we win.</p></div></div>
</div>
<div class="abs btn" style="left:145px;top:2759px;width:134px;height:38px">CONTACT US</div>
<div class="abs" style="left:631px;top:2540px;width:427px;height:259px;background:var(--tan)"></div>
<div class="abs photo" style="left:651px;top:2318px;width:387px;height:460px;background:linear-gradient(160deg,#dfe5e8 0%,#b7c2c8 40%,#4a5866 75%,#2c3a48 100%)" role="img" aria-label="Photo of two attorneys in suits talking in a bright modern office"></div>

<!-- PRACTICE AREAS -->
<div class="abs practice" role="img" aria-label="Photo of a firefighter attending to a wrecked car after a road accident" style="background:linear-gradient(90deg,#0d0d0d 0%,#1a1a1a 35%,#3b3733 60%,#5a4a30 80%,#2a2a2a 100%)"></div>
<div class="abs" style="left:0;top:2893px;width:1200px;height:662px;background:linear-gradient(180deg,rgba(0,0,0,.25),rgba(0,0,0,.45))"></div>
<h2 class="abs heading" style="left:142px;top:3012px;font-size:36px;color:var(--white)">Our Practice Areas</h2>

<div class="card featured" style="left:142px;top:3158px;width:220px;height:216px">
  <div style="display:flex;justify-content:space-between;width:100%;align-items:center">
    <span style="font-size:16px">Car Accidents</span>
    <svg width="40" height="34" viewBox="0 0 40 34" fill="none" stroke="#fff" stroke-width="1.8"><path d="M4 24v-7l4 -8h18l5 8h5v7z"/><circle cx="11" cy="25" r="4"/><circle cx="29" cy="25" r="4"/><path d="M30 4l2 4 4 -2-1 4 4 1-4 2"/></svg>
  </div>
  <p style="font-family:var(--sans);font-size:12px;line-height:19px;margin-top:28px;width:150px">We fight for victims of rear-end crashes, multi-vehicle collisions, pedestrian and cyclist accidents, and more.</p>
</div>
<div class="card" style="left:372px;top:3302px;width:220px;height:72px"><span>Slip and Fall /<br>Premises Liability</span>
  <svg width="36" height="32" viewBox="0 0 36 32" fill="none" stroke="#fff" stroke-width="1.8"><circle cx="20" cy="5" r="3"/><path d="M18 9l-6 8 8 3-4 10M18 9l6 8 6-2M4 30h28"/></svg></div>
<div class="card" style="left:604px;top:3302px;width:220px;height:72px"><span>Wrongful<br>Death</span>
  <svg width="30" height="34" viewBox="0 0 30 34" fill="none" stroke="#fff" stroke-width="1.8"><path d="M5 30V12a10 10 0 0 1 20 0v18zM2 32h26M15 10v12M10 15h10"/></svg></div>
<div class="card" style="left:836px;top:3302px;width:220px;height:72px"><span>Product<br>Liability</span>
  <svg width="30" height="34" viewBox="0 0 30 34" fill="none" stroke="#fff" stroke-width="1.8"><rect x="3" y="3" width="20" height="28" rx="2"/><path d="M8 10h10M8 16h10M8 22h6"/><circle cx="23" cy="24" r="5"/></svg></div>
<div class="card" style="left:142px;top:3389px;width:220px;height:74px"><span>Truck &amp; Commercial<br>Vehicle Accidents</span>
  <svg width="34" height="26" viewBox="0 0 34 26" fill="none" stroke="#fff" stroke-width="1.8"><path d="M2 4h18v14H2zM20 9h7l5 5v4H20z"/><circle cx="8" cy="20" r="3"/><circle cx="26" cy="20" r="3"/></svg></div>
<div class="card" style="left:372px;top:3389px;width:220px;height:74px"><span>Boating &amp; Watercraft<br>Accidents</span>
  <svg width="34" height="32" viewBox="0 0 34 32" fill="none" stroke="#fff" stroke-width="1.8"><path d="M17 2v20M17 4l10 14H17M4 22h26l-4 6H8zM2 31c4-2 6 2 10 0s6 2 10 0 6 2 10 0"/></svg></div>
<div class="card" style="left:604px;top:3389px;width:220px;height:74px"><span>Dog Bites and<br>Animal Attacks</span>
  <svg width="36" height="32" viewBox="0 0 36 32" fill="none" stroke="#fff" stroke-width="1.8"><circle cx="24" cy="5" r="3"/><path d="M22 9l-4 10 6 4v8M18 19l-6 4M6 20l4-4 6 2M4 28h10"/></svg></div>
<div class="card" style="left:836px;top:3389px;width:220px;height:74px"><span>Workplace<br>Injuries</span>
  <svg width="34" height="32" viewBox="0 0 34 32" fill="none" stroke="#fff" stroke-width="1.8"><path d="M6 12a8 8 0 0 1 16 0zM4 12h20"/><circle cx="14" cy="18" r="5"/><path d="M4 31c0-5 4-8 10-8s10 3 10 8M24 18h8v10h-8z"/></svg></div>

<!-- FLORIDA LAW -->
<div class="abs" style="left:119px;top:3650px;width:431px;height:534px;background:var(--tan)"></div>
<div class="abs photo" style="left:142px;top:3650px;width:409px;height:513px;background:linear-gradient(135deg,#e9e6e2 0%,#b8bcc2 35%,#2d4e78 65%,#1a2d55 100%)" role="img" aria-label="Photo of a person in a suit beside scales of justice and a gavel with digital binary overlay"></div>
<h2 class="abs heading" style="left:608px;top:3680px;font-size:36px">Florida Personal Injury Law</h2>
<div class="abs kicker" style="left:608px;top:3735px">Your Rights and Legal Protections</div>
<div class="abs" style="left:606px;top:3768px;width:440px">
  <div class="point"><div class="tick"><svg width="9" height="9" viewBox="0 0 10 10"><path d="M1.5 5.2l2.3 2.3 4.7-5" fill="none" stroke="#fff" stroke-width="1.8"/></svg></div>
    <div><h4>Comparative Negligence (Florida Statutes §768.81)</h4><p class="body">Even if you were partially at fault, you can still recover compensation. Your damages will be reduced based on your percentage of fault.</p></div></div>
  <div class="point" style="margin-top:22px"><div class="tick"><svg width="9" height="9" viewBox="0 0 10 10"><path d="M1.5 5.2l2.3 2.3 4.7-5" fill="none" stroke="#fff" stroke-width="1.8"/></svg></div>
    <div><h4>Statute of Limitations (Florida Statutes §95.11)</h4><p class="body">You have four years to file a personal injury claim and two years for wrongful death cases. Missing these deadlines can prevent you from recovering compensation.</p></div></div>
  <div class="point" style="margin-top:22px"><div class="tick"><svg width="9" height="9" viewBox="0 0 10 10"><path d="M1.5 5.2l2.3 2.3 4.7-5" fill="none" stroke="#fff" stroke-width="1.8"/></svg></div>
    <div><h4>Premises Liability (Florida Statutes §768.0755)</h4><p class="body">Property owners are responsible for dangerous conditions they knew or should have known about.</p></div></div>
</div>
<div class="abs btn" style="left:611px;top:4090px;width:134px;height:38px">CONTACT US</div>

<!-- CALL TO ACTION -->
<div class="abs" style="left:0;top:4274px;width:1200px;height:664px;background:var(--cream)"></div>
<h2 class="abs heading" style="left:0;top:4396px;width:1200px;text-align:center;font-size:34px">Take the First Step Toward Justice</h2>
<div class="abs" style="left:0;top:4455px;width:1200px;text-align:center;font-size:12.5px;color:var(--ink)">Let Us Fight for the Compensation You Deserve</div>
<div class="abs" style="left:0;top:4486px;width:1200px;text-align:center;font-size:12.5px;color:var(--ink)">If you have been injured due to someone else's negligence, do not wait. Time-sensitive deadlines could impact your case</div>

<div class="abs cta-box"></div>
<div class="cta-item" style="left:366px;top:4574px">
  <svg width="60" height="68" viewBox="0 0 60 68"><polygon points="30,3 57,18 57,50 30,65 3,50 3,18" fill="none" stroke="var(--tan)" stroke-width="2.5"/><path d="M30 47s-9-9-9-15a9 9 0 0 1 18 0c0 6-9 15-9 15z" fill="none" stroke="var(--tan)" stroke-width="2"/><circle cx="30" cy="32" r="3" fill="none" stroke="var(--tan)" stroke-width="2"/></svg>
  <span>Visit: <span class="plain">410 Ponce Court, Coral Gables, FL 33134</span></span>
</div>
<div class="cta-item" style="left:190px;top:4660px">
  <svg width="60" height="68" viewBox="0 0 60 68"><polygon points="30,3 57,18 57,50 30,65 3,50 3,18" fill="none" stroke="var(--tan)" stroke-width="2.5"/><rect x="19" y="24" width="22" height="20" rx="2" fill="none" stroke="var(--tan)" stroke-width="2"/><path d="M23 30h14M23 35h14M23 40h8" stroke="var(--tan)" stroke-width="2"/></svg>
  <span>Free Consultation</span>
</div>
<div class="cta-item" style="left:436px;top:4660px">
  <svg width="60" height="68" viewBox="0 0 60 68"><polygon points="30,3 57,18 57,50 30,65 3,50 3,18" fill="none" stroke="var(--tan)" stroke-width="2.5"/><circle cx="30" cy="34" r="11" fill="none" stroke="var(--tan)" stroke-width="2"/><path d="M22 26l16 16" stroke="var(--tan)" stroke-width="2"/></svg>
  <span>No Fees Unless We Win</span>
</div>
<div class="cta-item" style="left:718px;top:4660px">
  <svg width="60" height="68" viewBox="0 0 60 68"><polygon points="30,3 57,18 57,50 30,65 3,50 3,18" fill="none" stroke="var(--tan)" stroke-width="2.5"/><path d="M20 26l10-4 10 4v8c0 7-5 11-10 13-5-2-10-6-10-13z" fill="none" stroke="var(--tan)" stroke-width="2"/><path d="M25 34l4 4 6-7" fill="none" stroke="var(--tan)" stroke-width="2"/></svg>
  <span>Aggressive Representation</span>
</div>
<div class="cta-item" style="left:328px;top:4746px">
  <svg width="60" height="68" viewBox="0 0 60 68"><polygon points="30,3 57,18 57,50 30,65 3,50 3,18" fill="none" stroke="var(--tan)" stroke-width="2.5"/><path d="M22 28l8-8 6 6-8 8zM31 31l10 10M18 46h16" fill="none" stroke="var(--tan)" stroke-width="2"/></svg>
  <span>The Darrow Law Firm: <span class="plain">Where Justice Meets Dedication.</span></span>
</div>

<!-- FOOTER -->
<div class="abs footer"></div>
<div class="abs" style="left:0;top:4978px;width:1200px;text-align:center;font-family:var(--serif);font-size:34px;color:var(--white)">Darrow Law Firm</div>
<div class="abs fnav" style="left:275px">HOME</div>
<div class="abs fsep" style="left:344px">|</div>
<div class="abs fnav" style="left:373px">ABOUT US</div>
<div class="abs fsep" style="left:469px">|</div>
<div class="abs fnav" style="left:498px">PRACTICE AREAS</div>
<div class="abs fsep" style="left:638px">|</div>
<div class="abs fnav" style="left:668px">WHY CHOOSE US</div>
<div class="abs fsep" style="left:805px">|</div>
<div class="abs fnav" style="left:837px">CONTACT US</div>

<div class="abs fcontact" style="left:182px">
  <div class="fcircle"><svg width="16" height="12" viewBox="0 0 24 17"><rect x="1" y="1" width="22" height="15" rx="1" fill="none" stroke="#fff" stroke-width="2"/><path d="M1 1l11 8 11-8" fill="none" stroke="#fff" stroke-width="2"/></svg></div>
  <div>Email<br>info@darrowlawfirm.com</div>
</div>
<div class="abs fcontact" style="left:500px">
  <div class="fcircle"><svg width="14" height="18" viewBox="0 0 14 18"><path d="M7 17s-6-6-6-10a6 6 0 0 1 12 0c0 4-6 10-6 10z" fill="#fff"/><circle cx="7" cy="7" r="2" fill="#4a4a4a"/></svg></div>
  <div>Address<br>410 Ponce Court,<br>Coral Gables, FL 33134</div>
</div>
<div class="abs fcontact" style="left:797px">
  <div class="fcircle"><svg width="15" height="15" viewBox="0 0 24 24"><path d="M6.6 10.8a15 15 0 0 0 6.6 6.6l2.2-2.2a1 1 0 0 1 1-.25 11.4 11.4 0 0 0 3.6.6 1 1 0 0 1 1 1V20a1 1 0 0 1-1 1A17 17 0 0 1 3 4a1 1 0 0 1 1-1h3.5a1 1 0 0 1 1 1 11.4 11.4 0 0 0 .6 3.6 1 1 0 0 1-.25 1z" fill="#fff"/></svg></div>
  <div>Phone<br>(305) 555 0148</div>
</div>

<div class="abs" style="left:142px;top:5230px;width:916px;height:1px;background:#4a4a4a"></div>
<div class="abs" style="left:144px;top:5255px;font-size:11.5px;color:var(--white)">© 2025 The Darrow Law Firm. All Rights Reserved.</div>
<div class="abs social" style="left:917px"></div>
<div class="abs social" style="left:952px"></div>
<div class="abs social" style="left:987px"></div>
<div class="abs social" style="left:1022px"></div>

</body>
</html>
```